Youth deer hunt give away flyer.

We need a flyer designed for a youth deer hunt giveaway that we are doing. We are an Illinois whitetail deer hunting outfitter. We house and feed our clients as well as providing them with a guided deer hunt. It needs to include images as well as details about the giveaway. Im looking for a proffesional, looking flyer

Target Market(s)

rednecks, hunters

Industry/Entity Type

Hunting

Font styles to use
Serif
Sans Serif

Colors
000000
dbdbdb
ffffff
474747

Requirements
Must have
• not sure
Nice to have
• not sure
Should not have
• not sure

```html
<!DOCTYPE html>
<html lang="en">
<head>
<meta charset="UTF-8">
<title>2018 Youth Firearm Hunt – Hollow Creek Outfitting</title>
<link href="https://fonts.googleapis.com/css2?family=Smokum&family=Saira+Condensed:wght@700&family=Open+Sans:wght@400;600;800&display=swap" rel="stylesheet">
<style>
  :root{
    --gold-light:#f4c84e;
    --gold-dark:#d9a52f;
    --rust-dark:#7e2f17;
    --rust-mid:#a7431f;
    --rust-light:#c85a2a;
    --olive:#6b5a1e;
    --title-brown:#4a2810;
    --cream:#f6ead0;
    --accent-orange:#f3b23c;
    --ink:#1c1c1c;
    --ink-soft:#474747;
    --paper:#ffffff;
  }
  *{margin:0;padding:0;box-sizing:border-box}
  html,body{width:927px;height:1200px;overflow:hidden;background:var(--paper)}
  .flyer{position:relative;width:927px;height:1200px;overflow:hidden;font-family:"Open Sans",sans-serif}
  .backdrop{position:absolute;inset:0}
  .display-type{position:absolute;left:0;top:0;overflow:visible}
  .display-type text{font-family:"Smokum","Saira Condensed",sans-serif}
  .headline-text{font-size:100px;fill:var(--title-brown)}
  .dates-text{font-size:54px;fill:var(--paper)}
  .about-title-text{font-size:30px;fill:var(--accent-orange)}
  .perks{position:absolute;left:44px;top:322px;list-style:none;width:400px}
  .perks li{position:relative;padding-left:26px;margin-bottom:9px;white-space:nowrap;
    font-family:"Saira Condensed",sans-serif;font-weight:700;font-size:14px;line-height:24px;
    letter-spacing:.4px;color:var(--cream);text-transform:uppercase}
  .perks li::before{content:"";position:absolute;left:0;top:5px;width:14px;height:14px;border-radius:50%;
    background:#3a3a3a;border:2px solid #cfcfcf}
  .about{position:absolute;left:44px;top:550px;width:368px;color:var(--paper)}
  .about p{font-size:15px;line-height:22px;margin-bottom:9px}
  .photo{position:absolute}
  .brand{position:absolute;left:40px;top:1040px;width:285px;text-align:center;color:var(--ink);font-weight:600}
  .brand-mark{width:70px;height:70px;border-radius:50%;background:var(--ink);margin:0 auto 12px}
  .brand-name{font-size:31px;line-height:1;letter-spacing:1px;white-space:nowrap}
  .brand-sub{font-size:14px;letter-spacing:6px;margin-top:6px}
  .contact{position:absolute;left:346px;top:1030px;font-size:15px;line-height:22px;color:var(--ink-soft);font-style:normal}
  .contact .web{margin-top:6px}
  .social{display:flex;gap:8px;margin-top:6px}
  .social span{width:24px;height:24px;background:var(--ink-soft);border-radius:3px}
  .phone{position:absolute;right:36px;top:1134px;font-weight:800;font-size:35px;color:var(--ink);letter-spacing:.5px;white-space:nowrap}
</style>
</head>
<body>
<main class="flyer">
  <svg class="backdrop" width="927" height="1200" viewBox="0 0 927 1200" aria-hidden="true">
    <defs>
      <linearGradient id="rustFill" x1="0" y1="0" x2="1" y2="1">
        <stop offset="0" stop-color="#7e2f17"/>
        <stop offset=".55" stop-color="#a7431f"/>
        <stop offset="1" stop-color="#c85a2a"/>
      </linearGradient>
      <linearGradient id="goldFill" x1="0" y1="0" x2="1" y2="1">
        <stop offset="0" stop-color="#d9a52f"/>
        <stop offset=".6" stop-color="#f4c84e"/>
        <stop offset="1" stop-color="#f7d35c"/>
      </linearGradient>
    </defs>
    <rect width="927" height="1200" fill="url(#rustFill)"/>
    <path d="M0 0H927V310C800 330 640 325 520 305C350 275 160 190 0 135Z" fill="url(#goldFill)"/>
    <path d="M0 135C160 190 350 275 520 305C640 325 800 330 927 310" fill="none" stroke="#6b5a1e" stroke-width="7"/>
    <path d="M0 860C200 830 380 900 560 990C720 1065 850 1080 927 1060V1200H0Z" fill="#c85a2a"/>
    <path d="M0 905C200 880 380 955 550 1040C700 1105 850 1115 927 1095V1200H0Z" fill="#ffffff"/>
  </svg>

  <svg class="display-type" width="927" height="560" viewBox="0 0 927 560">
    <text class="headline-text" x="48" y="134" textLength="836" lengthAdjust="spacingAndGlyphs">2018 YOUTH FIREARM HUNT</text>
    <text class="dates-text" x="390" y="191" textLength="326" lengthAdjust="spacingAndGlyphs">OCTOBER 6-8, 2018</text>
    <text class="about-title-text" x="44" y="540" textLength="95" lengthAdjust="spacingAndGlyphs">ABOUT US</text>
  </svg>

  <ul class="perks">
    <li>4 night stay in our private cabin that include<br>meals for 2 parents and the child.</li>
    <li>Guided shotgun hunt on strictly managed properties.</li>
    <li>Ground blinds in place</li>
    <li>Permit and license fees are<br>the hunters responsibility.</li>
  </ul>

  <section class="about" aria-label="About us">
    <p>Hollow Creek Outfitting is a family owned and operated deer hunting outfitter located in Morgan and Scott Counties in west central Illinois. We provide low pressure, trophy whitetail hunts on privately owned farms across the region. The Hollis family are lifelong residents and hunters of Morgan County, with the family farm being established well over 150 years ago.</p>
    <p>To go along with guiding deer and turkey hunters, we also offer a wide variety of professional hunting services that include whitetail land consulting, scouting services, CRP and food plot plantings and more.</p>
  </section>

  <svg class="photo" style="left:478px;top:220px" width="440" height="440" viewBox="0 0 440 440" role="img" aria-label="Interior of the log cabin: pine walls, kitchen counter with stools, mounted deer heads and a dining table by glass doors">
    <defs>
      <linearGradient id="cabinTone" x1="0" y1="0" x2="0" y2="1">
        <stop offset="0" stop-color="#c98a45"/>
        <stop offset=".6" stop-color="#a86a32"/>
        <stop offset="1" stop-color="#6e4322"/>
      </linearGradient>
    </defs>
    <circle cx="220" cy="220" r="212" fill="url(#cabinTone)" stroke="#6b5a1e" stroke-width="8"/>
  </svg>

  <svg class="photo" style="left:455px;top:585px" width="500" height="500" viewBox="0 0 500 500" role="img" aria-label="Hunter posing in autumn woods with a large whitetail buck">
    <defs>
      <radialGradient id="woodsTone" cx=".5" cy=".5" r=".6">
        <stop offset="0" stop-color="#5a4a30"/>
        <stop offset=".7" stop-color="#3a3020"/>
        <stop offset="1" stop-color="#241c12"/>
      </radialGradient>
    </defs>
    <circle cx="250" cy="250" r="240" fill="url(#woodsTone)" stroke="#4a2412" stroke-width="8"/>
  </svg>

  <div class="brand">
    <div class="brand-mark"></div>
    <div class="brand-name">HOLLOW CREEK</div>
    <div class="brand-sub">OUTFITTING</div>
  </div>

  <address class="contact">
    Dale Hollis<br>
    1840 Creek Bend Road<br>
    Millbrook, Illinois 62000
    <div class="web">www.hollowcreekoutfitting.com<br>hollowcreekoutfitting@mailbox.com</div>
    <div class="social"><span></span><span></span></div>
  </address>

  <p class="phone">(217)555-0148</p>
</main>
</body>
</html>
```